postcard for Real Estate Agent that sells homes for less than any other agents

My company sells houses for a fraction of what others charge. I have most of the verbiage but I am open to ideas.
Our post card will be 6.25 x 9
We need an image that goes with our words and draws people to take a look
We are playful at the same time very serious about the money we will save our clients. In the past our message has been received as too good to be true. Our old message was "save $6000* when you list with us" We think the "*" was causing people to think their was a catch. Other agents will tell people that we will not do what they will do and that is why they must charge more. We are a full service agency and we will generally do everything that other agents will do and in many cases we will do more than other agents. We are changing this industry and need our message to get to every person that is thinking of selling their home

Target Market(s)

People who want to list their home for sale

Industry/Entity Type

Real Estate Agent

Requirements
Must have
• Image that makes people read the message

```html
<!DOCTYPE html>
<html lang="en">
<head>
<meta charset="utf-8">
<title>Keystone Realty – Listing Postcard</title>
<link rel="stylesheet" href="https://fonts.googleapis.com/css2?family=Archivo+Black&family=Arimo:wght@700&display=swap">
<style>
  :root {
    --navy: #163f73;
    --navy-text: #1d4677;
    --sky: #7fa9cf;
    --yellow: #fff200;
    --white: #ffffff;
    --shadow: #0a1d33;
    --photo-top: #d9d2c4;
    --photo-mid: #8f9aa8;
    --photo-low: #4d7a3a;
    --accent-green: #7dbb3f;
  }
  * { margin: 0; padding: 0; box-sizing: border-box; }
  html, body { width: 1200px; height: 800px; overflow: hidden; background: var(--white); }
  .postcard { position: relative; width: 1200px; height: 800px; font-family: "Arimo", Arial, sans-serif; font-weight: 700; }

  .hero-panel {
    position: absolute; left: 0; top: 0; width: 1200px; height: 600px;
    background: var(--navy);
    clip-path: polygon(0 0, 792px 0, 541px 600px, 0 600px);
  }
  .hero-photo {
    position: absolute; left: 0; top: 0; width: 1200px; height: 600px;
    background: linear-gradient(180deg, var(--photo-top) 0%, var(--photo-mid) 45%, var(--photo-low) 80%, #3e6a2c 100%);
    clip-path: polygon(806px 0, 1200px 0, 1200px 600px, 555px 600px);
  }

  .headline { position: absolute; left: 52px; top: 46px; color: var(--white); text-shadow: 3px 3px 0 var(--shadow); }
  .headline .lead { font-size: 39px; line-height: 44px; letter-spacing: -0.5px; }
  .headline .crazy { font-family: "Archivo Black", "Arial Black", sans-serif; font-size: 62px; line-height: 72px; color: var(--yellow); letter-spacing: 0.5px; }
  .headline .follow { font-size: 38px; line-height: 44px; letter-spacing: -0.5px; }

  .uses-title { position: absolute; left: 62px; top: 285px; font-size: 30px; line-height: 36px; color: var(--sky); letter-spacing: 0.3px; }
  .uses-title .amount { color: var(--white); }

  .uses-list { position: absolute; left: 64px; top: 364px; display: grid; grid-template-columns: 220px 200px; row-gap: 7px; list-style: none; color: var(--white); font-size: 17.5px; line-height: 19px; }
  .uses-list li { display: flex; align-items: center; gap: 8px; }
  .uses-list li::before { content: ""; width: 0; height: 0; border-left: 9px solid var(--sky); border-top: 5px solid transparent; border-bottom: 5px solid transparent; }

  .value-claim { position: absolute; left: 66px; top: 513px; font-size: 28px; line-height: 36px; color: var(--yellow); letter-spacing: 0.3px; }

  .brand { position: absolute; left: 96px; top: 668px; display: flex; align-items: center; gap: 14px; }
  .brand .mark { width: 34px; height: 34px; background: var(--accent-green); }
  .brand .name { font-size: 40px; color: var(--navy-text); letter-spacing: -0.5px; }

  .contact { position: absolute; left: 510px; top: 617px; width: 580px; text-align: center; color: var(--navy-text); }
  .contact .invite { font-size: 34px; line-height: 42px; }
  .contact .phone { font-family: "Archivo Black", "Arial Black", sans-serif; font-size: 76px; line-height: 86px; color: var(--sky); letter-spacing: 1px; }
  .contact .web { font-size: 31px; line-height: 40px; }
</style>
</head>
<body>
<main class="postcard">
  <div class="hero-panel"></div>
  <div class="hero-photo" role="img" aria-label="Smiling couple holding house keys in front of their home beside a sold sign and green hedge"></div>

  <h1 class="headline">
    <span class="lead">You’d have to be</span><br>
    <span class="crazy">Bat $#@T CRAZY</span><br>
    <span class="follow">to give an agent $6000.00</span><br>
    <span class="follow">To put a sign in your yard.</span>
  </h1>

  <h2 class="uses-title">Look at what you<br>can do with <span class="amount">$6000.00</span></h2>

  <ul class="uses-list">
    <li>Give it to your Kids</li><li>Build a fence</li>
    <li>Build a deck</li><li>Buy new clothes</li>
    <li>Landscape</li><li>Take a Vacation</li>
    <li>Pay off your car</li><li>Pay off student loan</li>
    <li>Buy New Carpet</li><li>Upgrade Appliances</li>
  </ul>

  <p class="value-claim">FULL SERVICE AGENCY AT A<br>FRACTION OF THE COST</p>

  <div class="brand">
    <span class="mark"></span>
    <span class="name">Keystone Realty</span>
  </div>

  <div class="contact">
    <p class="invite">Call Dale or Marcus at</p>
    <p class="phone">555.204.7391</p>
    <p class="web">www.DaleHomes.com</p>
  </div>
</main>
</body>
</html>
```